Dune Air & Plus business card

I need an awesome, double-sided business card designed with our new logo. I would like the one side black with the colored logo, and the back side is all yours. I'd like to see horizontal and vertical layouts. Get creative! Thank you.

Target Market(s)

HVAC, Heating and Cooling in Phoenix, AZ

Industry/Entity Type

HVAC

Contact Information for Business Card

We need our new logo on the card. Tom Harker, (623) 555-0142, tom@trydunesair.com, www.trydunesair.com, ROC 514273

```html
<!DOCTYPE html>
<html lang="en">
<head>
<meta charset="utf-8">
<title>Dune Air &amp; Plus — Business Card</title>
<link rel="stylesheet" href="https://fonts.googleapis.com/css2?family=Roboto:wght@400;700;900&display=swap">
<style>
  :root {
    --backdrop: #e9e9e9;
    --card: #1f1f1f;
    --card-edge: #2a2a2a;
    --orange: #ec6a1f;
    --blue: #1d72d8;
    --ink-light: #e6e6e6;
    --divider: #8a8a8a;
    --emboss-light: #474747;
    --emboss-mid: #2e2e2e;
    --emboss-dark: #161616;
  }
  * { box-sizing: border-box; margin: 0; padding: 0; }
  html, body { width: 1200px; height: 802px; overflow: hidden; }
  body {
    background: var(--backdrop);
    font-family: "Roboto", Arial, sans-serif;
    display: flex;
    align-items: center;
    justify-content: center;
    gap: 40px;
  }
  .card {
    width: 540px;
    height: 309px;
    background: var(--card);
    border: 1px solid var(--card-edge);
    position: relative;
    overflow: hidden;
    box-shadow: 0 10px 24px rgba(0,0,0,0.18);
  }

  /* Front */
  .card-front { display: flex; flex-direction: column; align-items: center; justify-content: center; gap: 34px; }
  .brand { display: flex; align-items: center; gap: 12px; }
  .brand-dot { width: 22px; height: 22px; border-radius: 50%; background: var(--orange); }
  .brand-name { color: var(--blue); font-weight: 900; font-size: 34px; letter-spacing: 0.5px; text-transform: uppercase; }
  .details { display: flex; align-items: center; gap: 18px; }
  .person { text-align: right; }
  .person-name { color: var(--orange); font-weight: 700; font-size: 19px; text-transform: uppercase; letter-spacing: 0.5px; }
  .person-license { color: var(--ink-light); font-size: 15px; margin-top: 4px; }
  .divider { width: 1.5px; height: 62px; background: var(--divider); }
  .contact-list { list-style: none; display: flex; flex-direction: column; gap: 5px; }
  .contact-item { display: flex; align-items: center; gap: 9px; color: var(--ink-light); font-size: 14px; }
  .contact-icon { width: 13px; height: 13px; flex: none; }

  /* Back */
  .card-back .back-brand {
    position: absolute; top: 34px; right: 40px;
    color: var(--blue); font-weight: 900; font-size: 34px;
    text-transform: uppercase; letter-spacing: 0.5px;
  }
  .card-back .emboss-art {
    position: absolute; left: 30px; right: 40px; bottom: 0; height: 185px;
    border-radius: 120px 120px 0 0;
    background:
      radial-gradient(ellipse at 55% 30%, var(--emboss-light) 0%, var(--emboss-mid) 45%, var(--emboss-dark) 100%);
    box-shadow: inset 0 2px 3px rgba(255,255,255,0.08), inset 0 -8px 18px rgba(0,0,0,0.5), 0 -1px 2px rgba(0,0,0,0.6);
  }
</style>
</head>
<body>

  <section class="card card-front" aria-label="Business card front">
    <div class="brand">
      <span class="brand-dot"></span>
      <span class="brand-name">Dune Air &amp; Plus</span>
    </div>
    <div class="details">
      <div class="person">
        <p class="person-name">Tom Harker</p>
        <p class="person-license">ROC 514273</p>
      </div>
      <span class="divider"></span>
      <ul class="contact-list">
        <li class="contact-item">
          <svg class="contact-icon" viewBox="0 0 16 16" aria-hidden="true"><path d="M4 1.5l2.2 3-1.4 1.6c.9 2 2.4 3.6 4.4 4.5l1.6-1.4 3 2.2-1.3 2.6C7 13.5 2.5 9 1.5 3z" fill="var(--orange)"/></svg>
          (623) 555-0142
        </li>
        <li class="contact-item">
          <svg class="contact-icon" viewBox="0 0 16 16" aria-hidden="true"><rect x="1.5" y="3.5" width="13" height="9" fill="none" stroke="var(--orange)" stroke-width="1.4"/><path d="M1.5 3.5l6.5 5 6.5-5" fill="none" stroke="var(--orange)" stroke-width="1.4"/></svg>
          tom@trydunesair.com
        </li>
        <li class="contact-item">
          <svg class="contact-icon" viewBox="0 0 16 16" aria-hidden="true"><circle cx="8" cy="8" r="6.5" fill="none" stroke="var(--orange)" stroke-width="1.4"/><path d="M1.5 8h13M8 1.5c-3 3.5-3 9.5 0 13M8 1.5c3 3.5 3 9.5 0 13" fill="none" stroke="var(--orange)" stroke-width="1.2"/></svg>
          www.trydunesair.com
        </li>
      </ul>
    </div>
  </section>

  <section class="card card-back" aria-label="Business card back">
    <p class="back-brand">Dune Air &amp; Plus</p>
    <div class="emboss-art" role="img" aria-label="Large dark embossed illustration of a house with garage doors under a sun"></div>
  </section>

</body>
</html>
```